Dryer Vent Cleaning Postcard Design

We need a postcard design for Flue Wranglers, a company that specializes in dryer vent cleaning, repairs and upgrades. Dryer vents need periodic cleaning to avoid lint clogging, dryer malfunction, long dry times and even a house fire. This card will be sent to residential and businesses prospects to introduce them to our services and the importance of maintaining their dryer vents. Our website is @ fluewrangling.com and provides information about our services, photos of our work and our general color scheme (purple/orange). Final print size will be 5x7 horizontal.

Target Market(s)

homeowners and business owners (spas, salons, grooming, gyms, laundrymats, etc)

Requirements
Must have
• Reduce the risk of fire
shortened dry times
lower energy consumption
18000 dryer fires caused in the US per year
Nice to have
• Does your dryer take too long to dry?

```html
<!DOCTYPE html>
<html lang="en">
<head>
<meta charset="utf-8">
<title>Flue Wranglers Postcard</title>
<link href="https://fonts.googleapis.com/css2?family=Antonio:wght@200;400;700&family=Lato:wght@400;700&display=swap" rel="stylesheet">
<style>
:root{
  --purple:#3e3566;
  --orange:#f3864a;
  --ink:#4a4453;
  --lilac:#d9d3f0;
  --paper:#f4f4f6;
  --stage:#efefef;
  --art-tan:#b7a58d;
  --art-grey:#a9a6ad;
}
*{margin:0;padding:0;box-sizing:border-box}
html,body{width:771px;height:1200px;overflow:hidden;background:var(--stage)}
.card{position:absolute;left:46px;width:689px;height:495px;background:var(--paper);overflow:hidden;box-shadow:0 8px 30px rgba(0,0,0,.18)}
.card--front{top:54px}
.card--back{top:606px}
.shape{position:absolute;left:0;top:0;width:689px;height:495px}
.top-band{position:absolute;left:0;top:0;width:689px;height:35px;background:var(--purple)}
.abs{position:absolute;white-space:nowrap}
.condensed{font-family:'Antonio',sans-serif;text-transform:uppercase;line-height:1}
.headline-light{left:48px;top:64px;font-size:44px;font-weight:200;color:var(--ink)}
.headline-bold{left:45px;top:112px;font-size:52px;font-weight:700;color:var(--ink)}
.brand{left:432px;top:176px;display:flex;align-items:center;gap:10px;font-family:'Lato',sans-serif;font-weight:700;font-size:26px;color:var(--purple)}
.brand-dot{width:22px;height:22px;border-radius:50%;background:var(--orange)}
.art{position:absolute;border-radius:6px}
.art--cart{left:28px;top:242px;width:118px;height:226px;background:linear-gradient(180deg,var(--art-tan) 0 45%,#d9302f 45%)}
.benefits{left:162px;top:260px;list-style:none}
.benefits li{display:flex;align-items:center;gap:11px;height:54px;font-family:'Antonio',sans-serif;text-transform:uppercase;font-size:21px;font-weight:400;color:var(--orange)}
.benefits svg{width:32px;height:32px;flex:none}
.stat{left:133px;top:424px;width:300px;text-align:center;font-size:16px;font-weight:400;color:#fff;line-height:1.4}
.pill{position:absolute;background:var(--orange);color:#fff;border-radius:20px;font-family:'Lato',sans-serif;text-align:center;box-shadow:0 6px 10px rgba(0,0,0,.2)}
.pill--front{left:463px;top:336px;width:171px;height:36px;line-height:36px;font-size:18px}
.pill b{font-weight:700}
.email{left:419px;top:386px;width:260px;text-align:center;font-family:'Lato',sans-serif;font-size:17px;color:#fff}
.site{font-family:'Lato',sans-serif;font-weight:700;color:var(--orange);text-align:center}
.site--front{left:450px;top:419px;width:200px;font-size:18px}
.social{left:518px;top:455px;display:flex;gap:14px}
.social span{width:15px;height:15px;border-radius:50%;border:2px solid var(--lilac)}
.tagline-light{left:47px;top:48px;font-size:44px;font-weight:200;color:var(--lilac)}
.tagline-bold{left:49px;top:96px;font-size:42px;font-weight:700;color:var(--lilac)}
.services{left:328px;top:42px;list-style:none}
.services li{height:44.5px;font-family:'Antonio',sans-serif;text-transform:uppercase;font-size:18px;color:var(--orange)}
.services li::before{content:"• "}
.art--standing{left:502px;top:27px;width:170px;height:243px;background:linear-gradient(180deg,var(--orange) 0 6%,var(--art-tan) 6%)}
.pill--back{left:54px;top:246px;width:200px;height:42px;line-height:42px;font-size:21px;font-weight:700}
.site--back{left:57px;top:294px;width:200px;font-size:20px}
.service-title{left:278px;top:309px;font-family:'Lato',sans-serif;font-weight:700;font-size:29px;color:var(--orange)}
.art--lifter{left:18px;top:345px;width:200px;height:150px;background:linear-gradient(180deg,var(--art-tan),#9e8a72)}
.art--dryer{left:313px;top:356px;width:350px;height:139px;background:linear-gradient(90deg,#2b3a66 0 15%,var(--art-grey) 15%)}
</style>
</head>
<body>

<section class="card card--front">
  <svg class="shape" viewBox="0 0 689 495" aria-hidden="true">
    <path d="M0,228 C150,182 300,226 420,268 C520,300 600,298 689,242 L689,495 L0,495 Z" fill="#3e3566"/>
    <path d="M0,252 C100,205 220,210 293,238 C200,218 100,230 0,285 Z" fill="#0d0d12"/>
    <path d="M474,286 C580,300 650,262 689,186 L689,248 C640,290 560,300 474,286 Z" fill="#f3864a"/>
  </svg>
  <div class="top-band"></div>
  <h1 class="abs condensed headline-light">Does your dryer take</h1>
  <h2 class="abs condensed headline-bold">Too long to dry?</h2>
  <div class="abs brand"><span class="brand-dot"></span>Flue Wranglers</div>
  <div class="art art--cart" role="img" aria-label="Illustrated technician pushing a red vent-cleaning vacuum"></div>
  <ul class="abs benefits">
    <li><svg viewBox="0 0 34 34" fill="none" stroke="#f3864a" stroke-width="1.6"><path d="M17 3c2 6 10 9 10 18a10 10 0 0 1-20 0c0-5 3-7 4-11 1 3 2 4 4 5 0-5 0-8 2-12z"/></svg>Reduce the risk of fire</li>
    <li><svg viewBox="0 0 34 34" fill="none" stroke="#f3864a" stroke-width="1.6"><path d="M29 17a12 12 0 1 1-4-9"/><path d="M25 4v5h5"/><path d="M16 10v8h5"/></svg>Shortened dry times</li>
    <li><svg viewBox="0 0 34 34" fill="none" stroke="#f3864a" stroke-width="1.6"><circle cx="17" cy="17" r="14"/><path d="M19 6l-7 12h6l-3 10 8-13h-6z"/></svg>Lower energy consumption</li>
  </ul>
  <p class="abs condensed stat">18000 dryer fires<br>caused in the US per year</p>
  <div class="pill pill--front">tel:<b>555-014-2290</b></div>
  <p class="abs email">office@fluewrangling.com</p>
  <p class="abs site site--front">fluewrangling.com</p>
  <div class="abs social" aria-label="Social links"><span></span><span></span><span></span></div>
</section>

<section class="card card--back">
  <svg class="shape" viewBox="0 0 689 495" aria-hidden="true">
    <path d="M0,0 L689,0 L689,240 C600,296 520,298 420,268 C300,230 150,178 0,212 Z" fill="#3e3566"/>
    <path d="M0,202 C100,170 220,170 293,218 C200,194 100,196 0,238 Z" fill="#0d0d12"/>
    <path d="M474,286 C580,300 650,262 689,186 L689,248 C640,290 560,300 474,286 Z" fill="#f3864a"/>
  </svg>
  <h2 class="abs condensed tagline-light">We do one thing,</h2>
  <h2 class="abs condensed tagline-bold">&amp; we do it right</h2>
  <ul class="abs services">
    <li>Dryer vent cleaning</li>
    <li>Dryer vent installation</li>
    <li>Bird nest removal</li>
    <li>Vent cap replacement</li>
  </ul>
  <div class="art art--standing" role="img" aria-label="Illustrated technician holding a vent brush over his shoulder"></div>
  <div class="pill pill--back">tel:555-014-2290</div>
  <p class="abs site site--back">fluewrangling.com</p>
  <p class="abs service-title">Dryer Vent Cleaning &amp; Repair</p>
  <div class="art art--lifter" role="img" aria-label="Illustrated technician holding a long vent-cleaning rod"></div>
  <div class="art art--dryer" role="img" aria-label="Illustration of a vent brush, wall vent, duct hose and clothes dryer"></div>
</section>

</body>
</html>
```